QAMARIN AL-RIYAH MEDICAL CO
QAMARIN AL-RIYAH
Project: QAMARIN AL-RIYAH MEDICAL CO
QAMARIN AL-RIYAH MEDICAL CO - Pharmacy/Pharmaceuticals
Creative Brief
Use same font as used in my logo
HUDA KERMANI
Sales & Marketing Director
P.O Box 4137 Dammam 31276 Saudi Arabia
huda@qrm.med.example
www.qrm.med.example

```html
<!DOCTYPE html>
<html lang="en">
<head>
<meta charset="utf-8">
<title>Qamarin Al-Riyah Business Card</title>
<link rel="stylesheet" href="https://fonts.googleapis.com/css2?family=Marcellus&family=Open+Sans:wght@400;600;700&display=swap">
<style>
  :root {
    --backdrop: #e4e4e4;
    --card-black: #0d0d0d;
    --frame-grey: #bdbdbd;
    --brand-red: #c8383a;
    --white: #ffffff;
    --soft-grey: #9a9a9a;
    --line-grey: #8c8c8c;
    --icon-grey: #555555;
  }
  * { box-sizing: border-box; margin: 0; padding: 0; }
  html, body {
    width: 1200px; height: 908px; overflow: hidden;
    background: var(--backdrop);
  }
  .canvas {
    position: relative; width: 1200px; height: 908px;
    display: flex; flex-direction: column; align-items: center; justify-content: center; gap: 56px;
  }
  .card {
    position: relative; width: 620px; height: 354px;
    background: var(--card-black);
    box-shadow: 0 10px 24px rgba(0,0,0,.22);
    overflow: hidden;
  }

  /* Front */
  .front-frame {
    position: absolute; inset: 24px;
    border: 6px solid var(--frame-grey);
  }
  .front-frame::after {
    content: ""; position: absolute; inset: 8px;
    border: 2px solid var(--frame-grey);
  }
  .brand {
    position: absolute; inset: 0;
    display: flex; align-items: center; justify-content: center; gap: 14px;
    font-family: "Marcellus", serif; color: var(--white);
    font-size: 34px; letter-spacing: 1px;
  }
  .brand-dot {
    width: 14px; height: 14px; border-radius: 50%; background: var(--brand-red); flex: none;
  }

  /* Back */
  .back-brand {
    position: absolute; left: 40px; top: 62px;
    display: flex; align-items: center; gap: 10px;
    font-family: "Marcellus", serif; color: var(--white); font-size: 20px;
  }
  .back-brand .brand-dot { width: 10px; height: 10px; }
  .name-band {
    position: absolute; left: 300px; right: 0; top: 52px; height: 62px;
    background: var(--brand-red); padding: 8px 22px;
    font-family: "Open Sans", sans-serif; color: var(--white);
  }
  .person-name { font-size: 22px; font-weight: 700; letter-spacing: .5px; line-height: 1.1; }
  .person-role { font-size: 17px; font-weight: 400; line-height: 1.3; white-space: nowrap; }
  .contacts {
    position: absolute; left: 322px; top: 130px;
    font-family: "Open Sans", sans-serif; color: var(--white);
    font-size: 13px; line-height: 1.35;
  }
  .contact-group { margin-bottom: 8px; }
  .bottom-rule {
    position: absolute; left: 0; right: 0; top: 281px; height: 3px; background: var(--line-grey);
  }
  .bottom-band {
    position: absolute; left: 0; right: 0; bottom: 0; height: 54px; background: var(--brand-red);
  }
  .icon-row {
    position: absolute; left: 360px; top: 268px; display: flex; gap: 80px;
  }
  .icon-disc {
    width: 28px; height: 28px; border-radius: 50%;
    background: var(--white); border: 2px solid var(--soft-grey);
    display: flex; align-items: center; justify-content: center;
  }
</style>
</head>
<body>
<main class="canvas">
  <section class="card card-front">
    <div class="front-frame"></div>
    <div class="brand"><span class="brand-dot"></span><span>QAMARIN AL-RIYAH</span></div>
  </section>

  <section class="card card-back">
    <div class="back-brand"><span class="brand-dot"></span><span>QAMARIN AL-RIYAH</span></div>
    <div class="name-band">
      <div class="person-name">HUDA KERMANI</div>
      <div class="person-role">Sales &amp; Marketing Director</div>
    </div>
    <div class="contacts">
      <div class="contact-group"><div>013 555 0142</div><div>013 555 0143</div></div>
      <div class="contact-group"><div>huda@qrm.med.example</div><div>www.qrm.med.example</div></div>
      <div class="contact-group"><div>P.O Box 4137 Dammam 31276</div><div>Saudi Arabia</div></div>
    </div>
    <div class="bottom-rule"></div>
    <div class="bottom-band"></div>
    <div class="icon-row">
      <div class="icon-disc">
        <svg width="14" height="14" viewBox="0 0 24 24" aria-label="phone"><path fill="#555" d="M6.6 10.8a15 15 0 0 0 6.6 6.6l2.2-2.2c.3-.3.7-.4 1-.2 1.1.4 2.3.6 3.6.6.6 0 1 .4 1 1V20c0 .6-.4 1-1 1A17 17 0 0 1 3 4c0-.6.4-1 1-1h3.5c.6 0 1 .4 1 1 0 1.3.2 2.5.6 3.6.1.3 0 .7-.2 1z"/></svg>
      </div>
      <div class="icon-disc">
        <svg width="14" height="14" viewBox="0 0 24 24" aria-label="web"><circle cx="12" cy="12" r="9" fill="none" stroke="#555" stroke-width="2"/><path d="M3 12h18M12 3c3 3 3 15 0 18M12 3c-3 3-3 15 0 18" fill="none" stroke="#555" stroke-width="1.6"/></svg>
      </div>
      <div class="icon-disc">
        <svg width="14" height="14" viewBox="0 0 24 24" aria-label="location"><path fill="#555" d="M12 2a7 7 0 0 0-7 7c0 5 7 13 7 13s7-8 7-13a7 7 0 0 0-7-7zm0 9.5A2.5 2.5 0 1 1 12 6.5a2.5 2.5 0 0 1 0 5z"/></svg>
      </div>
    </div>
  </section>
</main>
</body>
</html>
```